INNOVATIVE DESIGN NEEDED FOR FINANCIAL COMPANY

INTERNATIONAL FIRM IN HONG KONG NEEDS A MODERN BUSINESS CARD DESIGN. ONE SIDE ENGLISH OTHER SIDE IN CHINESE. WE ARE OPEN TO CHANGING FONTS AND COLOR. SHOULD BE A CARD THAT IS PROFESSIONAL DEALING WITH HIGH NET WORTH CLIENTELE. BOTH SIDES OF THE CARD WILL BE THE SAME, HOWEVER, THE WORDING ON ONE SIDE WILL BE ENGLISH AND THE OTHER SIDE IN CHINESE (CAN ASSIST IN THE LETTERING - CAN PROVIDE ONCE CARD DESIGN IS ACCEPTED.

Target Market(s)

Hong Kong/CHINA

Contact Information for Business Card

ATTRACTIVE MODERN

```html
<!DOCTYPE html>
<html lang="en">
<head>
<meta charset="utf-8">
<title>Linden Crest Wealth – Business Cards</title>
<link rel="stylesheet" href="https://fonts.googleapis.com/css2?family=Montserrat:wght@400;500;700&family=Noto+Sans+TC:wght@400;700&display=swap">
<style>
  :root {
    --stage: #e9e7e3;
    --card-dark: #26282a;
    --card-dark-hi: #3a3d40;
    --card-light: #ffffff;
    --accent: #1fae84;
    --ink-light: #f2f2f2;
    --ink-dark: #4a4a4a;
    --ink-muted: #8a8a8a;
  }
  * { box-sizing: border-box; margin: 0; padding: 0; }
  html, body { width: 1200px; height: 1023px; overflow: hidden; }
  body {
    background: var(--stage);
    font-family: "Montserrat", "Noto Sans TC", sans-serif;
    position: relative;
  }
  .card {
    position: absolute;
    width: 580px;
    height: 331px;
    border-radius: 4px;
    box-shadow: 0 10px 30px rgba(0,0,0,.18);
    padding: 48px 46px;
  }
  .card--english {
    left: 90px; top: 110px;
    background: linear-gradient(135deg, var(--card-dark) 0%, var(--card-dark-hi) 50%, var(--card-dark) 100%);
    color: var(--ink-light);
  }
  .card--chinese {
    left: 530px; top: 560px;
    background: var(--card-light);
    color: var(--ink-dark);
  }
  .brand { display: flex; align-items: center; gap: 16px; }
  .brand__dot { width: 52px; height: 52px; border-radius: 50%; background: var(--accent); flex: none; }
  .brand__name { font-weight: 700; font-size: 25px; letter-spacing: 1px; line-height: 1.2; }
  .brand__sub { font-weight: 700; font-size: 12px; letter-spacing: 2.5px; margin-top: 4px; }
  .card--chinese .brand__name, .card--chinese .brand__sub { color: var(--ink-dark); }
  .details { display: flex; align-items: center; margin-top: 52px; }
  .person { width: 200px; text-align: right; padding-right: 22px; }
  .person__name { color: var(--accent); font-size: 26px; font-weight: 500; letter-spacing: 1px; }
  .person__title { font-size: 17px; margin-top: 4px; }
  .card--chinese .person__title { color: var(--accent); font-size: 15px; }
  .divider { width: 2px; height: 100px; background: var(--accent); flex: none; }
  .contact { padding-left: 22px; font-size: 13px; line-height: 1.75; list-style: none; }
  .card--chinese .contact { color: var(--ink-muted); }
  .contact li { display: flex; align-items: center; gap: 9px; }
  .contact svg { width: 12px; height: 12px; flex: none; fill: var(--accent); }
  .contact .plain { padding-left: 21px; }
</style>
</head>
<body>
  <section class="card card--english" aria-label="English side">
    <div class="brand">
      <span class="brand__dot"></span>
      <div>
        <div class="brand__name">林峰財富管理有限公司</div>
        <div class="brand__sub">LINDEN CREST WEALTH LTD</div>
      </div>
    </div>
    <div class="details">
      <div class="person">
        <div class="person__name">ALEX CHAN</div>
        <div class="person__title">Manager</div>
      </div>
      <span class="divider"></span>
      <ul class="contact">
        <li class="plain">12 Harbour View Tower</li>
        <li class="plain">Canton Rd, HONG KONG</li>
        <li><svg viewBox="0 0 12 12"><path d="M3 1l2 2.5-1 1.5a7 7 0 0 0 3 3l1.5-1L11 9l-1 2C5 11 1 7 1 2z"/></svg>852-5550-0142</li>
        <li><svg viewBox="0 0 12 12"><path d="M1 2h10v8H1zM1.5 2.5L6 6.5l4.5-4" stroke="#26282a" stroke-width="1"/></svg>alex.chan@lcwealth.com</li>
        <li><svg viewBox="0 0 12 12"><circle cx="6" cy="6" r="5.5"/></svg>www.lcwealth.com</li>
      </ul>
    </div>
  </section>

  <section class="card card--chinese" aria-label="Chinese side" lang="zh-Hant">
    <div class="brand">
      <span class="brand__dot"></span>
      <div>
        <div class="brand__name">林峰財富管理有限公司</div>
        <div class="brand__sub">LINDEN CREST WEALTH LTD</div>
      </div>
    </div>
    <div class="details">
      <div class="person">
        <div class="person__name">陳志明</div>
        <div class="person__title">經理</div>
      </div>
      <span class="divider"></span>
      <ul class="contact">
        <li><svg viewBox="0 0 12 12"><path d="M3 1l2 2.5-1 1.5a7 7 0 0 0 3 3l1.5-1L11 9l-1 2C5 11 1 7 1 2z"/></svg>852-5550-0142</li>
        <li><svg viewBox="0 0 12 12"><path d="M1 2h10v8H1zM1.5 2.5L6 6.5l4.5-4" stroke="#ffffff" stroke-width="1"/></svg>alex.chan@lcwealth.com</li>
        <li><svg viewBox="0 0 12 12"><circle cx="6" cy="6" r="5.5"/></svg>www.lcwealth.com</li>
        <li class="plain">香港尖沙咀廣東道海景大廈12號</li>
      </ul>
    </div>
  </section>
</body>
</html>
```